Webdesign für Industrieanlagenbau-Unternehmen
Zielgruppe
Die ZEV services GmbH ist ein ein österreichisches, eigentümergeführtes Industrieanlagenbau-Unternehmen mit Niederlassungen an derzeit 2 Standorten (Traiskirchen/NÖ und Hallein/Sbg) und ist in den Geschäftsfeldern Industrieanlagenbau, Reinraumtechnik und Sondermaschinenbau - sowie im Projekt- und Behördenmanagement tätig.
Die ZEV services GmbH unterstützt ihre B2B-Kunden bei der Umsetzung von Engineering-Projekten in der Hightech-, Elektronik- und Prozessindustrie.
Unsere Kernkompetenzen sind Konzepterstellung, 3D-Planung, Konstruktion, Design und Montage von Prozessanlagen und Reinräumen, eine eigene Fertigung und Prototypenbau in unserer „Metall-& Kunststoff Manufaktur“ sowie die Abwicklung des Behörden-Managements wie z.B. Einreichverfahren nach Gewerbeordnung.
Langjährige und dauerhafte Geschäftsbeziehungen zu unseren Kunden stehen bei uns im Vordergrund.
Zielsgruppe der neuen website:
„Visitenkarte“ der ZEV services GmbH
potentielle Mitarbeiter („Employer Branding“), Ingenieure/Projektmanager (WI-Maschinenbau, Elektro- und Prozesstechnik), Mechatroniker, Schlosser, Elektriker
B2B Kunden aus Bereichen Mikroelektronik-Fertigung, chemische Industrie, Lebensmittel- und Pharmaproduktion
Bestandskunden (Stakeholder des „Buying Centers“ bei Kunden)
Neukunden „eingeschränkt“ (dzt. Keine aktive Kundenakquise via web geplant)
Aufgabenstellung
Allgemeine Anforderungen an die neue website:
Ziel sind eher „schlanke“ Texte & Design (vgl. https://www.valdrin-gruppe.com/de/)
Produkt- und Leistungsspezifisches Bildmaterial sollen hauptsächlich ZEV-eigene Fotos und Videos sein (Stock-Fotos nur für Allgemeine Bilder). Beispielhaftes Bildmaterial (sollte durch ZEV Mitarbeiter dann im CMS einfach ausgetauscht werden können) in diesen Unterlagen
CMS (Content Management System) zur Administration durch ZEV Mitarbeiter
Hosting auf europäischen ServernServern (z.B. https://voll-pack.com/, https://www.brommlat.com, https://www.kessfurt.de, https://www.ornix2go.com/, https://www.puvo.at)
Basierend auf weitverbreiteten open-Source Systemen (z.B. Wordpress , Joomla, TYPO3)
Responsive Webdesign – eine Website für alle Geräte (PC, Tablet, Smartphone) und alle gängigen Browser (Chrome, Edge, Safari, Firefox, Opera, Internet Explorer)
Google Pagespeed mind. 85 Punkte, GTmetrix Grade > 80%
Sicherheitszertifikat (SSL-Zertifikat)
Sprache – Deutsch, Englisch
E-Commerce-Gesetz (ECG) & DSGVO konform (Cookie Disclaimer Standard „nur notwendige“)
Impressum
AGB - Allgemeine Lieferungs- und Zahlungsbedingungen
Sitemap
Vollständige Rechte an der website (Design, Inhalt etc.) bei ZEV services GmbH
Einbettung von Text, Fotos und Videos durch ZEV Mitarbeiter
Hinzufügen von Menü-Unterpunkten durch ZEV Mitarbeiter

```html
<!DOCTYPE html>
<html lang="de">
<head>
<meta charset="utf-8">
<title>ZEV services GmbH – Wir bauen Ihre Anlagen</title>
<link href="https://fonts.googleapis.com/css2?family=Lato:wght@300;400;700;900&display=swap" rel="stylesheet">
<style>
  :root{
    --red:#e3221f;
    --blue:#1d5c9b;
    --hero-dark:#123e86;
    --hero-light:#3a78c8;
    --white:#ffffff;
    --footer-bg:#efefef;
    --footer-bottom:#f6f6f6;
    --text-grey:#555555;
  }
  *{margin:0;padding:0;box-sizing:border-box}
  html,body{width:1200px;height:2315px;overflow:hidden;background:var(--white)}
  body{font-family:'Lato',Arial,sans-serif;position:relative;color:var(--white)}
  .page-bg{position:absolute;left:0;top:0}
  .nav{position:absolute;top:0;left:0;width:1200px;height:76px}
  .nav-logo{position:absolute;left:163px;top:13px;width:50px;height:50px;border-radius:50%;background:var(--white);
    color:var(--red);font-weight:900;font-size:15px;display:flex;align-items:center;justify-content:center}
  .nav-link{position:absolute;top:28px;font-size:13px;font-weight:700;letter-spacing:.2px;color:var(--white)}
  .flag{position:absolute;top:29px;width:15px;height:10px}
  .hero-title{position:absolute;top:340px;left:0;width:1200px;text-align:center;font-size:63px;font-weight:300;letter-spacing:-1.5px}
  .hero-title b{font-weight:900}
  .slider-dots{position:absolute;top:446px;left:546px;display:flex;gap:4px}
  .slider-dots span{width:19px;height:3px;background:var(--white)}
  .slider-dots span.active{background:var(--red)}
  .badge{position:absolute;left:552px;top:493px;width:96px;height:96px;border-radius:50%;background:rgba(255,255,255,.35);
    display:flex;align-items:center;justify-content:center}
  .badge-inner{width:84px;height:84px;border-radius:50%;background:var(--white);color:var(--red);font-weight:900;font-size:24px;
    display:flex;align-items:center;justify-content:center}
  .about-title{position:absolute;top:597px;left:0;width:1200px;text-align:center;font-size:34px;font-weight:700}
  .about-col{position:absolute;top:660px;font-size:12.6px;line-height:19.5px;text-align:justify}
  .about-col p{margin-bottom:19.5px}
  .about-col.left{left:161px;width:431px}
  .about-col.right{left:627px;width:413px}
  .section-title{position:absolute;left:0;width:1200px;text-align:center;font-size:34px;font-weight:900}
  .services-title{top:1019px;color:var(--blue)}
  .gallery-title{top:1673px;color:var(--red)}
  .hex-label{position:absolute;width:253px;text-align:center;font-size:18px;font-weight:700;color:var(--white)}
  .hex-button{position:absolute;left:528px;top:1250px;width:144px;height:36px;border:2px solid var(--white);
    font-size:14px;font-weight:700;display:flex;align-items:center;justify-content:center}
  .gallery{position:absolute;left:161px;top:1748px;width:876px;display:grid;grid-template-columns:repeat(3,1fr);gap:1px}
  .gallery div{height:194px}
  .footer{position:absolute;left:0;top:2187px;width:1200px;height:74px;background:var(--footer-bg)}
  .footer-brand{position:absolute;left:163px;top:20px;display:flex;align-items:center;gap:8px;color:var(--red);font-size:30px;font-weight:900}
  .footer-brand i{width:30px;height:30px;border-radius:50%;background:var(--red);display:block}
  .footer-links{position:absolute;right:160px;top:27px;display:flex;gap:15px;font-size:11.5px;color:var(--text-grey)}
  .copyright{position:absolute;left:0;top:2261px;width:1200px;height:54px;background:var(--footer-bottom);
    text-align:center;line-height:54px;font-size:11.5px;color:var(--text-grey)}
</style>
</head>
<body>
<svg class="page-bg" width="1200" height="960" viewBox="0 0 1200 960">
  <defs>
    <linearGradient id="heroGrad" x1="0" y1="0" x2="1" y2="1">
      <stop offset="0" stop-color="var(--hero-dark)"/>
      <stop offset="1" stop-color="var(--hero-light)"/>
    </linearGradient>
  </defs>
  <rect width="1200" height="540" fill="url(#heroGrad)" role="img" aria-label="Industrieanlage mit Rohrleitungen in Blau getönt"/>
  <polygon points="0,434 600,521 1200,434 1200,845 600,953 0,845" fill="var(--red)"/>
</svg>

<header class="nav">
  <div class="nav-logo">ZEV</div>
  <span class="nav-link" style="left:265px">HOME-ZEV</span>
  <span class="nav-link" style="left:401px">LEISTUNGEN</span>
  <span class="nav-link" style="left:540px">JOBS/KARRIERE</span>
  <span class="nav-link" style="left:701px">KUNDEN-PORTAL</span>
  <span class="nav-link" style="left:871px">KONTAKT</span>
  <svg class="flag" style="left:993px" viewBox="0 0 15 10" aria-label="English">
    <rect width="15" height="10" fill="#1f3b8a"/><path d="M0 0L15 10M15 0L0 10" stroke="#fff" stroke-width="2"/>
    <path d="M7.5 0V10M0 5H15" stroke="#fff" stroke-width="3"/><path d="M7.5 0V10M0 5H15" stroke="#d02030" stroke-width="1.6"/>
  </svg>
  <svg class="flag" style="left:1023px" viewBox="0 0 15 10" aria-label="Deutsch">
    <rect width="15" height="3.4" fill="#000"/><rect y="3.3" width="15" height="3.4" fill="#dd0000"/><rect y="6.6" width="15" height="3.4" fill="#ffce00"/>
  </svg>
</header>

<h1 class="hero-title">Wir <b>bauen</b> Ihre <b>Anlagen</b></h1>
<div class="slider-dots"><span class="active"></span><span></span><span></span><span></span><span></span></div>

<div class="badge"><div class="badge-inner">ZEV</div></div>
<h2 class="about-title">Wer wir sind</h2>
<div class="about-col left">
  <p>Die ZEV servicesGmbH ist ein österreichisches Industrieanlagenbau-Unternehmen und unterstützt Sie bei der Umsetzung von Engineering-Projekten in der Hightech-, Elektronik-und Prozessindustrie.</p>
  <p>Unsere Kernkompetenzen sind Konzepterstellung, 3D-Planung, Konstruktion, Design und Montage von Prozessanlagen und Reinräumen.</p>
  <p>Wir betreiben eine eigene Fertigung und Prototypenbau in unserer „Metall-&amp; Kunststoff Manufaktur“ und unterhalten einen eigenen Fuhrpark für unsere Montageteams.</p>
</div>
<div class="about-col right">
  <p>Abhängig von der Projektgröße sichern wir als Generalunternehmer (GU) die effiziente Ausführung Ihres Vorhabens und setzen das Projekt vollständig um –„Fire&amp; Forget“.<br>Wir übernehmen auch die Abwicklung des Behörden-Managements wie z.B. Einreichverfahren nach Gewerbeordnung (GewO).</p>
  <p>Langfristige, verlässliche und vertrauensvolle Geschäftsbeziehungen zu unseren Kunden stehen bei uns im Vordergrund.</p>
</div>

<h2 class="section-title services-title">Leistungen</h2>
<svg class="page-bg" style="top:1080px" width="1200" height="522" viewBox="0 1080 1200 522">
  <defs>
    <linearGradient id="hexBlue" x1="0" y1="0" x2="0" y2="1">
      <stop offset="0" stop-color="#4a6a98"/><stop offset="1" stop-color="#223f78"/>
    </linearGradient>
    <linearGradient id="hexRed" x1="0" y1="0" x2="0" y2="1">
      <stop offset="0" stop-color="#d6484b"/><stop offset="1" stop-color="#c85356"/>
    </linearGradient>
  </defs>
  <g stroke="#fff" stroke-width="5">
    <polygon role="img" aria-label="Maschinenanlage" fill="url(#hexBlue)" points="342,1083 469,1156 469,1302 342,1375 215,1302 215,1156"/>
    <polygon role="img" aria-label="Sondermaschinen in Halle" fill="url(#hexBlue)" points="858,1083 985,1156 985,1302 858,1375 731,1302 731,1156"/>
    <polygon role="img" aria-label="Hände über Diagrammen am Laptop" fill="url(#hexBlue)" points="470,1306 597,1379 597,1525 470,1598 343,1525 343,1379"/>
    <polygon role="img" aria-label="Kran an Gasversorgungsanlage" fill="url(#hexBlue)" points="729,1306 856,1379 856,1525 729,1598 602,1525 602,1379"/>
    <polygon role="img" aria-label="Reinraum in Rot getönt" fill="url(#hexRed)" points="600,1083 727,1156 727,1302 600,1375 473,1302 473,1156"/>
  </g>
</svg>
<span class="hex-label" style="left:216px;top:1270px">Industrieanlagenbau</span>
<span class="hex-label" style="left:474px;top:1203px">Reinraumtechnik</span>
<span class="hex-button">Erfahren Sie mehr</span>
<span class="hex-label" style="left:732px;top:1270px">Sondermaschinenbau</span>
<span class="hex-label" style="left:344px;top:1488px">Projekt-Management</span>
<span class="hex-label" style="left:605px;top:1488px">Gasversorgungsanlagen</span>

<h2 class="section-title gallery-title">Galerie</h2>
<div class="gallery">
  <div role="img" aria-label="Hand mit Tablet und Cloud-Symbol" style="background:radial-gradient(circle at 50% 40%,#3d7fd8,#0c1f4a 70%)"></div>
  <div role="img" aria-label="Geschäftsmann mit Tablet und Diagrammen" style="background:linear-gradient(135deg,#2d3e5c,#cfd8e2)"></div>
  <div role="img" aria-label="Hände zeigen auf Diagramme am Laptop" style="background:linear-gradient(135deg,#d8cfc2,#2a2a2e)"></div>
  <div role="img" aria-label="Fertigungshalle von oben" style="background:linear-gradient(160deg,#6d6a66,#3a3632)"></div>
  <div role="img" aria-label="Bagger und Schutzhelm bei Sonnenuntergang" style="background:linear-gradient(180deg,#e8a640,#b26a1e 60%,#4a3a2a)"></div>
  <div role="img" aria-label="Brückenbaustelle mit Kränen" style="background:linear-gradient(180deg,#9cc4e8,#d8c89a 60%,#4c6a5c)"></div>
</div>

<footer class="footer">
  <div class="footer-brand"><i></i>ZEV</div>
  <nav class="footer-links"><span>Impressum</span><span>AGB</span><span>Datenschutz</span><span>Nachhaltigkeit</span></nav>
</footer>
<div class="copyright">© ZEV services GmbH</div>
</body>
</html>
```